Bref créative
RON TALIVERO STATIONARY PACKAGE
Letterhead paper, Envelopes, Business Cards, Patient brochures, Flyer,Gift Certificate, T-Shirts
Professional
RON TALIVERO DDS
General & Cosmetic Dentistry
47-30 91 Street
Elmhurst, NY 11208
brightcuspdental@mailbox-example.com
www.brightcuspdental-example.com
I would like to present a very professional image for my company.
Smile!

```html
<!DOCTYPE html>
<html lang="en">
<head>
<meta charset="utf-8">
<title>Bright Cusp Dental Stationery Package</title>
<link href="https://fonts.googleapis.com/css2?family=Open+Sans:wght@400;600;700&family=Parisienne&display=swap" rel="stylesheet">
<style>
  :root{
    --backdrop:#4a3a30;
    --paper:#ffffff;
    --green:#8cbf26;
    --gold:#c9b21c;
    --ink:#333333;
    --ink-soft:#8a8a8a;
    --charcoal:#232323;
    --panel:#4b4b4b;
  }
  *{box-sizing:border-box;margin:0;padding:0}
  html,body{width:1200px;height:826px;overflow:hidden}
  body{background:var(--backdrop);position:relative;font-family:"Open Sans",Arial,sans-serif;color:var(--ink)}
  .piece{position:absolute;background:var(--paper);box-shadow:0 2px 6px rgba(0,0,0,.35);overflow:hidden}
  .brand{font-family:"Open Sans",Arial,sans-serif;font-weight:700;color:var(--green);line-height:1.1;display:flex;align-items:center;gap:5px;white-space:nowrap}
  .brand::before{content:"";width:8px;height:8px;border-radius:50%;background:var(--green);flex:none}
  .small{font-size:6px;line-height:1.5;color:var(--ink-soft)}
  .script{font-family:"Parisienne",cursive}
  .photo{position:absolute}

  /* business cards */
  .card{width:150px;height:86px}
  .card .brand{position:absolute;left:10px;top:12px;font-size:10px}
  .card .name{position:absolute;left:23px;top:28px;font-size:6.5px;font-weight:700;white-space:nowrap}
  .card .info{position:absolute;left:10px;bottom:8px;white-space:nowrap}
  .card-dark{background:var(--charcoal)}
  .card-dark .brand{left:auto;right:10px}
  .card-dark .info{left:auto;right:10px;text-align:right;color:#bdbdbd;font-size:5.5px}

  /* envelopes */
  .envelope-back{position:absolute;left:36px;top:240px}
  .envelope-front{left:36px;top:392px;width:294px;height:214px}
  .envelope-front .brand{position:absolute;left:14px;top:18px;font-size:13px}
  .envelope-front .return{position:absolute;left:14px;top:44px}
  .envelope-front .band{position:absolute;left:0;right:0;bottom:16px;height:3px;background:var(--green)}
  .envelope-front .band.gold{bottom:12px;height:2px;background:var(--gold)}
  .envelope-front .web{position:absolute;right:14px;bottom:23px;font-size:6px;color:var(--ink-soft)}

  /* letterhead */
  .letterhead{left:365px;top:31px;width:415px;height:625px}
  .letterhead .brand{position:absolute;left:30px;top:32px;font-size:15px}
  .letterhead .return{position:absolute;right:30px;top:34px;text-align:right}
  .letterhead .body{position:absolute;left:30px;right:30px;top:130px;font-size:7px;line-height:1.6;color:#666}
  .letterhead .body p{margin-bottom:10px}
  .letterhead .signature{position:absolute;left:30px;top:300px;font-size:22px;color:#555}
  .letterhead .web{position:absolute;left:0;right:0;bottom:26px;text-align:center;font-size:6px;color:var(--ink-soft)}
  .letterhead .band{position:absolute;left:0;right:0;bottom:14px;height:4px;background:var(--green)}
  .letterhead .band.gold{bottom:8px;height:3px;background:var(--gold)}

  /* gift certificates */
  .gift{top:662px;width:350px;height:100px}
  .gift .brand{position:absolute;left:10px;top:16px;font-size:9px}
  .gift .contact{position:absolute;left:10px;top:50px}
  .gift .divider{position:absolute;left:112px;top:10px;bottom:10px;width:1px;background:#ddd}
  .gift .title{position:absolute;left:170px;top:6px;font-size:19px;color:var(--ink)}
  .gift .fields{position:absolute;left:124px;right:16px;top:38px;font-size:6px;color:#555}
  .gift .field{display:flex;gap:6px;align-items:flex-end;height:12px}
  .gift .field span{width:36px}
  .gift .field i{flex:1;border-bottom:1px solid #ccc;height:8px}

  /* flyers */
  .flyer{left:852px;width:313px;height:362px}
  .headline{font-weight:700;font-size:13px;line-height:1.15;white-space:nowrap}
  .headline .green{color:var(--green)}
  .headline .gold{color:var(--gold)}
  .flyer .footer{position:absolute;left:0;right:0;bottom:0;height:10px;background:var(--green)}
  .flyer .footer.gold{background:var(--gold)}
  .side-panel{position:absolute;background:var(--panel);padding:8px}
</style>
</head>
<body>

<!-- business cards -->
<section class="piece card" style="left:43px;top:31px">
  <div class="brand">Bright Cusp Dental</div>
  <div class="name">RON TALIVERO DDS</div>
  <div class="info small">General &amp; Cosmetic Dentistry</div>
</section>
<section class="piece card card-dark" style="left:200px;top:31px">
  <div class="brand" style="top:12px">Bright Cusp Dental</div>
  <div class="info small">12 Lantern Row<br>Brookvale, ST 00000<br>brightcuspdental@mailbox-example.com<br>www.brightcuspdental-example.com</div>
</section>
<section class="piece card" style="left:43px;top:127px">
  <div class="brand">Bright Cusp Dental</div>
  <div class="name">Ron Talivero</div>
  <div class="info small">12 Lantern Row, Brookvale, ST 00000</div>
</section>
<section class="piece card card-dark" style="left:200px;top:127px">
  <div class="brand" style="top:12px">Bright Cusp Dental</div>
  <div class="info small">General &amp; Cosmetic Dentistry<br>www.brightcuspdental-example.com</div>
</section>

<!-- envelope backs -->
<svg class="envelope-back" width="294" height="150" viewBox="0 0 294 150" aria-hidden="true">
  <rect x="0" y="0" width="294" height="80" fill="#ffffff"/>
  <polygon points="0,0 294,0 147,60" fill="#c9b21c"/>
  <rect x="0" y="70" width="294" height="80" fill="#ffffff"/>
  <polygon points="0,70 294,70 147,132" fill="#8cbf26"/>
  <text x="147" y="40" text-anchor="middle" font-family="Open Sans, sans-serif" font-size="8" font-weight="700" fill="#ffffff">Bright Cusp Dental</text>
  <text x="147" y="108" text-anchor="middle" font-family="Open Sans, sans-serif" font-size="8" font-weight="700" fill="#ffffff">Bright Cusp Dental</text>
</svg>

<!-- envelope front -->
<section class="piece envelope-front">
  <div class="brand">Bright Cusp Dental</div>
  <div class="return small">12 Lantern Row<br>Brookvale, ST 00000</div>
  <div class="web">www.brightcuspdental-example.com</div>
  <div class="band"></div><div class="band gold"></div>
</section>

<!-- letterhead -->
<section class="piece letterhead">
  <div class="brand">Bright Cusp Dental</div>
  <div class="return small">12 Lantern Row<br>Brookvale, ST 00000<br>brightcuspdental@mailbox-example.com</div>
  <div class="body">
    <p>Dear Patient,</p>
    <p>Thank you for choosing our practice for your dental care. Our team is committed to gentle, modern treatment and clear advice at every visit.</p>
    <p>We offer cleanings, whitening, fillings and cosmetic work in a calm setting. Please call our office to book your next appointment.</p>
    <p>We look forward to seeing you and your family soon.</p>
  </div>
  <div class="signature script">Signature</div>
  <div class="web">www.brightcuspdental-example.com</div>
  <div class="band"></div><div class="band gold"></div>
</section>

<!-- gift certificates -->
<section class="piece gift" style="left:36px">
  <div class="brand">Bright Cusp Dental</div>
  <div class="contact small">12 Lantern Row<br>Brookvale, ST 00000</div>
  <div class="divider"></div>
  <div class="title script">Gift Certificate</div>
  <div class="fields">
    <div class="field"><span>To:</span><i></i></div>
    <div class="field"><span>From:</span><i></i></div>
    <div class="field"><span>Amount:</span><i></i></div>
    <div class="field"><span>Signature:</span><i></i><span style="width:auto">Date:</span><i style="flex:.5"></i></div>
  </div>
</section>
<section class="piece gift" style="left:400px">
  <div class="brand">Bright Cusp Dental</div>
  <div class="contact small">12 Lantern Row<br>Brookvale, ST 00000</div>
  <div class="divider"></div>
  <div class="title script">Gift Certificate</div>
  <div class="fields">
    <div class="field"><span>To:</span><i></i></div>
    <div class="field"><span>From:</span><i></i></div>
    <div class="field"><span>Amount:</span><i></i></div>
    <div class="field"><span>Signature:</span><i></i><span style="width:auto">Date:</span><i style="flex:.5"></i></div>
  </div>
</section>

<!-- flyer front -->
<section class="piece flyer" style="top:31px">
  <div class="brand" style="position:absolute;left:12px;top:14px;font-size:11px">Bright Cusp Dental</div>
  <div class="headline" style="position:absolute;left:12px;top:40px"><span class="green">LOREM IPSUM</span><br><span class="gold">DOLOR SITE AMIT</span></div>
  <div class="photo" role="img" aria-label="Close-up photo of a bright smile" style="left:160px;top:10px;width:143px;height:84px;background:linear-gradient(135deg,#f1e3d6,#c98e7a)"></div>
  <div class="photo" role="img" aria-label="Photo of a smiling family of three" style="left:12px;top:104px;width:186px;height:140px;background:linear-gradient(160deg,#e9d2b9,#b57f5e 70%,#7a5a45)"></div>
  <div class="side-panel small" style="left:204px;top:104px;width:99px;height:140px;color:#e0e0e0">Healthy smiles for the whole family, from first checkups to cosmetic care.</div>
  <div class="photo" role="img" aria-label="Photo of dental treatment" style="left:12px;top:254px;width:90px;height:86px;background:linear-gradient(135deg,#e7e2dc,#a6b6c2)"></div>
  <div class="photo" role="img" aria-label="Photo of a patient at a dental checkup" style="left:108px;top:254px;width:90px;height:86px;background:linear-gradient(135deg,#efe6dd,#b8a08d)"></div>
  <div class="footer"></div>
</section>

<!-- flyer back -->
<section class="piece flyer" style="top:402px">
  <div class="photo" role="img" aria-label="Photo of a smiling family of three" style="left:0;top:0;width:313px;height:150px;background:linear-gradient(160deg,#f0dcc6,#bf8a68 65%,#82604a)"></div>
  <div style="position:absolute;left:0;right:0;top:150px;height:22px;background:var(--gold);padding:4px 12px;color:#fff;font-weight:700;font-size:12px;white-space:nowrap">BRIGHT CUSP DENTAL</div>
  <div class="headline" style="position:absolute;left:12px;top:182px"><span class="green">LOREM IPSUM</span><br><span class="gold">DOLOR SITE AMIT</span></div>
  <p class="small" style="position:absolute;left:12px;top:222px;width:150px">Gentle care and modern treatment in a friendly office.</p>
  <div class="photo" role="img" aria-label="Photo of a mother and child smiling" style="left:180px;top:182px;width:123px;height:90px;background:linear-gradient(135deg,#ecdccb,#a98a72)"></div>
  <div class="small" style="position:absolute;left:12px;top:290px">12 Lantern Row<br>Brookvale, ST 00000<br>www.brightcuspdental-example.com</div>
  <div class="footer gold"></div>
</section>

</body>
</html>
```